Professional IT Company Letterhead

We need a new letterhead design to incorporate our new login and business card design recently received here on Sketch Guild. We want the same look and feel as the other two accepted projects. We want a professional and clean design.

Target Market(s)

Medical/Dental and Professional Services Businesses (CPA, Attorney, Architect etc)

Industry/Entity Type

Business

Requirements
Must have
• Clean and professional, consistent brand with our current design of our new logo and business cards.
Nice to have
• Would like to also be able to use the design on our newsletter header

```html
<!DOCTYPE html>
<html lang="en">
<head>
<meta charset="utf-8">
<title>Reefline Technology Letterhead</title>
<link href="https://fonts.googleapis.com/css2?family=Arimo:wght@400;700&family=Quicksand:wght@500&display=swap" rel="stylesheet">
<style>
  :root {
    --brand-blue: #0875bb;
    --logo-blue: #1a9ad9;
    --paper: #ffffff;
    --footer-text: #ffffff;
  }
  html, body {
    margin: 0;
    padding: 0;
    overflow: hidden;
    background: var(--paper);
  }
  .letterhead {
    position: relative;
    width: 927px;
    height: 1200px;
    background: var(--paper);
    overflow: hidden;
    font-family: "Arimo", Arial, sans-serif;
  }
  .top-notch {
    position: absolute;
    left: 151px;
    top: 0;
  }
  .brand {
    position: absolute;
    left: 50px;
    top: 66px;
    width: 260px;
  }
  .brand-row {
    display: flex;
    align-items: center;
    gap: 10px;
  }
  .brand-mark {
    flex: none;
    width: 54px;
    height: 54px;
    border-radius: 50%;
    background: var(--logo-blue);
  }
  .brand-name {
    margin: 0;
    font-family: "Arimo", Arial, sans-serif;
    font-weight: 700;
    font-size: 21px;
    line-height: 1;
    color: var(--logo-blue);
    white-space: nowrap;
  }
  .brand-tagline {
    margin: 10px 0 0;
    font-family: "Quicksand", Arial, sans-serif;
    font-weight: 500;
    font-size: 10px;
    letter-spacing: 1.5px;
    white-space: nowrap;
    color: var(--logo-blue);
  }
  .footer-band {
    position: absolute;
    left: 0;
    top: 1085px;
    width: 927px;
    height: 115px;
    background: var(--brand-blue);
    color: var(--footer-text);
  }
  .footer-notch {
    position: absolute;
    left: 76px;
    top: 0;
  }
  .company-name {
    position: absolute;
    left: 97px;
    top: 36px;
    margin: 0;
    font-size: 15px;
    font-weight: 400;
  }
  .contact-row {
    position: absolute;
    top: 58px;
    left: 0;
    width: 927px;
    height: 16px;
    font-size: 11px;
  }
  .contact-item {
    position: absolute;
    display: flex;
    align-items: center;
    gap: 6px;
    white-space: nowrap;
    line-height: 16px;
  }
  .contact-item svg { flex: none; }
  .divider {
    position: absolute;
    top: 1px;
    width: 1px;
    height: 14px;
    background: var(--footer-text);
  }
</style>
</head>
<body>
<div class="letterhead">
  <svg class="top-notch" width="55" height="24" viewBox="0 0 55 24" aria-hidden="true">
    <polygon points="0,0 55,0 27.5,24" fill="var(--brand-blue)"/>
  </svg>

  <header class="brand">
    <div class="brand-row">
      <div class="brand-mark" aria-hidden="true"></div>
      <p class="brand-name">Reefline Technology</p>
    </div>
    <p class="brand-tagline">IT Support for Medical &amp; Dental Practices</p>
  </header>

  <footer class="footer-band">
    <svg class="footer-notch" width="45" height="20" viewBox="0 0 45 20" aria-hidden="true">
      <polygon points="0,0 45,0 22.5,20" fill="var(--paper)"/>
    </svg>
    <p class="company-name">Company Name (Pvt) Ltd.</p>
    <div class="contact-row">
      <div class="contact-item" style="left:96px">
        <svg width="9" height="12" viewBox="0 0 9 12" aria-hidden="true">
          <path d="M4.5 0C2 0 0 2 0 4.4 0 7.5 4.5 12 4.5 12S9 7.5 9 4.4C9 2 7 0 4.5 0z" fill="#fff"/>
          <circle cx="4.5" cy="4.4" r="1.6" fill="var(--brand-blue)"/>
        </svg>
        <span>2207/54 Harbour Lane, Brisbane QLD 4000</span>
      </div>
      <span class="divider" style="left:341px"></span>
      <div class="contact-item" style="left:357px">
        <svg width="10" height="12" viewBox="0 0 10 12" aria-hidden="true">
          <path d="M2.2 0.5 L4 3 3 4.3C3.6 6 4.6 7.3 6.2 8.3L7.4 7.4 9.6 9.4 8.4 11.3C4.2 10.8 0.6 6.2 0.6 1.8z" fill="#fff"/>
        </svg>
        <span>+11 (62) 480 917</span>
      </div>
      <span class="divider" style="left:485px"></span>
      <div class="contact-item" style="left:503px">
        <svg width="15" height="10" viewBox="0 0 15 10" aria-hidden="true">
          <rect x="0.5" y="0.5" width="14" height="9" fill="none" stroke="#fff"/>
          <path d="M0.5 0.5 7.5 6 14.5 0.5" fill="none" stroke="#fff"/>
        </svg>
        <span>info@reeflinetech.com</span>
      </div>
      <span class="divider" style="left:666px"></span>
      <div class="contact-item" style="left:683px">
        <svg width="11" height="11" viewBox="0 0 11 11" aria-hidden="true">
          <circle cx="5.5" cy="5.5" r="5.5" fill="#fff"/>
          <path d="M0 5.5H11M5.5 0V11M2 2.5Q5.5 4 9 2.5M2 8.5Q5.5 7 9 8.5" stroke="var(--brand-blue)" stroke-width="0.7" fill="none"/>
        </svg>
        <span>www.reeflinetech.com</span>
      </div>
    </div>
  </footer>
</div>
</body>
</html>
```